Indoor Gun Range Web Design Project

Create a professional bold indoor gun range website. Logo colors are white, red, and black. This is a very professional gun range. Please use high quality stock images if possible. Stay away from a lot of militia type photos. Use your best judgement on what to put as a main image and headline.

Here are some websites that I like for design.

http://www.harborlinefirearms.example/
http://www.pagecrafthub.example/website-templates/51947.html
http://www.brightmarkworks.example/

Target Market(s)

Men ages 25-65

Industry/Entity Type

Gun

Requirements
Must have
• Bold lettering, logo attached, exciting photos.
Should not have
• A lot of militia photos.

```html
<!DOCTYPE html>
<html lang="en">
<head>
<meta charset="utf-8">
<title>True Mark Indoor Range</title>
<link href="https://fonts.googleapis.com/css2?family=Arimo:wght@400;700&family=Russo+One&display=swap" rel="stylesheet">
<style>
:root{
  --red:#d4161c;
  --red-dark:#a50d12;
  --ink:#1c1c1c;
  --text:#444;
  --muted:#888;
  --hero-bg:#eeeeee;
  --band:#3a3c3f;
  --band-dark:#2a2b2d;
  --footer:#1d1e20;
  --footer-text:#8a8a8a;
  --white:#ffffff;
  --green:#8cc63f;
}
*{box-sizing:border-box;margin:0;padding:0}
html,body{width:980px;height:1200px;overflow:hidden}
body{font-family:"Arimo",Arial,sans-serif;background:var(--footer);position:relative;color:var(--text)}
.topnav{position:absolute;left:0;top:0;width:980px;height:42px;background:linear-gradient(#e0262b,var(--red-dark));display:flex;align-items:center;padding:0 98px}
.topnav ul{display:flex;list-style:none}
.topnav li{color:var(--white);font-weight:700;font-size:14px;padding:0 11px;height:42px;line-height:42px}
.topnav li:first-child{padding-left:0}
.topnav li.active{background:var(--red-dark);border-bottom:3px solid #7d0a0e}
.account{margin-left:auto;display:flex;gap:28px;color:#f5d0d0;font-size:11.5px}
.hero{position:absolute;top:42px;left:0;width:980px;height:451px;background:radial-gradient(ellipse at 60% 40%,#fafafa,var(--hero-bg))}
.hero-photo{position:absolute;left:56px;top:130px;width:370px;height:321px;background:linear-gradient(160deg,#6a6a6a,#2e2e2e 60%,#b89a86)}
.brand{position:absolute;left:98px;top:40px;display:flex;align-items:center;gap:12px}
.brand-name{font-family:"Russo One",sans-serif;font-size:24px;color:var(--ink);line-height:1.05;width:230px}
.brand-dot{width:40px;height:40px;border-radius:50%;background:var(--red)}
.social{position:absolute;right:60px;top:30px;display:flex;gap:7px}
.social span{width:36px;height:36px;border-radius:50%;background:#333}
.slide-arrow{position:absolute;top:165px}
.hero-copy{position:absolute;left:451px;top:284px;width:420px}
.hero-copy h1{font-family:"Russo One",sans-serif;color:var(--red);font-size:35px;font-weight:400;letter-spacing:.5px}
.hero-copy p{font-size:15px;line-height:17px;color:#333;margin-top:4px;width:405px}
.btn-join{display:inline-block;margin-top:18px;width:203px;height:39px;line-height:37px;text-align:center;border-radius:4px;background:linear-gradient(#a5d85a,#72a82c);border:1px solid #5f8e22;color:#1f3a05;font-weight:700;font-size:17px}
.features{position:absolute;top:493px;left:0;width:980px;height:386px;background:radial-gradient(ellipse at 50% 30%,#4a4c50,var(--band-dark));border-top:4px solid #222}
.card{position:absolute;top:35px;width:186px;height:312px;background:var(--white);border-radius:3px;overflow:hidden;box-shadow:0 2px 6px rgba(0,0,0,.5)}
.card h2{height:48px;background:linear-gradient(#e52a2f,var(--red-dark));color:var(--white);font-size:16px;font-weight:700;display:flex;align-items:center;padding-left:12px;gap:8px}
.card-photo{height:148px}
.card-body{padding:10px 14px;font-size:10px;line-height:13px;color:#555}
.ticks li{list-style:none;display:flex;gap:6px;margin-bottom:10px}
.more{position:absolute;bottom:16px;left:28px;height:20px;padding:0 24px 0 12px;border-radius:10px;background:linear-gradient(#f2f2f2,#d6d6d6);font-size:10px;line-height:20px;color:var(--red-dark)}
.more::after{content:"";position:absolute;right:6px;top:5px;width:10px;height:10px;border-radius:50%;background:var(--red)}
.caption{position:absolute;left:0;top:183px;width:186px;background:rgba(0,0,0,.7);color:#eee;font-size:12.5px;line-height:15px;padding:8px 12px}
.news-item{display:flex;gap:6px;padding:10px 4px 8px 0;border-bottom:1px solid #e2e2e2}
.news-date{width:28px;flex:none;text-align:center;font-size:9px;color:#999}
.news-date b{display:block;background:#3b3b3b;color:#fff;font-size:13px;height:22px;line-height:22px}
.news-item h3{font-size:10.5px;color:#222;margin-bottom:2px;white-space:nowrap}
.news-item p{font-size:9.5px;line-height:12px;color:#666}
.footer{position:absolute;top:879px;left:0;width:980px;height:321px}
.foot-head{position:absolute;top:44px;color:var(--red);font-size:13.5px;font-weight:400;display:flex;align-items:center;gap:8px}
.foot-head::before{content:"";width:11px;height:11px;border-radius:50%;background:var(--red)}
.links{position:absolute;top:76px;list-style:none;font-size:10px;line-height:14px;color:var(--footer-text)}
.links li::before{content:"• ";color:#666}
.links li.gap{margin-top:12px}
.links li.hot{color:var(--red)}
.mail{position:absolute;left:426px;top:76px;width:200px;font-size:9.5px;color:#aaa}
.mail .field{margin-top:6px;width:190px;height:20px;background:#fff;border-radius:2px}
.mail .subscribe{display:inline-block;margin-top:6px;padding:2px 10px;border-radius:10px;background:#e8e8e8;color:var(--red);font-size:10px}
.share{margin-top:14px;width:188px;height:30px;background:#f4f4f4;border-radius:2px;display:flex;align-items:center;gap:6px;padding:0 10px}
.share span{height:16px;border-radius:2px;background:#dcdcdc;border:1px solid #bbb}
.foot-brand{position:absolute;left:672px;top:56px;display:flex;align-items:center;gap:10px;opacity:.35}
.foot-brand .brand-name{color:#777;font-size:17px;width:170px}
.foot-brand .brand-dot{background:#555;width:34px;height:34px}
.foot-rule{position:absolute;left:0;top:213px;width:980px;border-top:1px solid #2e2f31}
.copyright{position:absolute;left:98px;top:236px;font-size:9.5px;line-height:14px;color:#777}
</style>
</head>
<body>
<nav class="topnav">
  <ul>
    <li>HOME</li><li>RANGE FEES</li><li class="active">RANGE RULES</li><li>RANGE NEWS</li><li>MEMBERSHIP</li><li>CONTACT</li>
  </ul>
  <div class="account"><span>Sign In</span><span>Sign Up</span></div>
</nav>

<header class="hero">
  <div class="hero-photo" role="img" aria-label="Photo of a hand holding a large black pistol pointed toward the viewer"></div>
  <div class="brand"><span class="brand-name">TRUE MARK INDOOR RANGE</span><span class="brand-dot"></span></div>
  <div class="social"><span></span><span></span></div>
  <svg class="slide-arrow" style="left:64px" width="24" height="40" viewBox="0 0 24 40"><polyline points="20,2 4,20 20,38" fill="none" stroke="#c4c4c4" stroke-width="4"/></svg>
  <svg class="slide-arrow" style="right:64px" width="24" height="40" viewBox="0 0 24 40"><polyline points="4,2 20,20 4,38" fill="none" stroke="#c4c4c4" stroke-width="4"/></svg>
  <div class="hero-copy">
    <h1>INDOOR GUN RANGE!</h1>
    <p>Lorem ipsum dolor sit amet, consectetur adipiscing elit. Praesent elementum dui id. Consectetur adipiscing sed non est eu lectus adipiscing hendrerit.</p>
    <span class="btn-join">Join Membership!</span>
  </div>
</header>

<section class="features">
  <article class="card" style="left:97px">
    <h2>Featured Rules</h2>
    <div class="card-photo" role="img" aria-label="Photo of a man in a white tank top holding a pistol in front of city buildings" style="background:linear-gradient(#8a96a3,#3f4850)"></div>
    <ul class="card-body ticks">
      <li><svg width="14" height="12" viewBox="0 0 14 12"><polyline points="1,6 5,10 13,1" fill="none" stroke="#6aa121" stroke-width="2.5"/></svg>Lorem ipsum dolor sit amet, conse ctetur adipis cing elit.</li>
      <li><svg width="14" height="12" viewBox="0 0 14 12"><polyline points="1,6 5,10 13,1" fill="none" stroke="#6aa121" stroke-width="2.5"/></svg>Lorem ipsum dolor sit amet, conse ctetur adipis cing elit.</li>
    </ul>
    <span class="more">Learn More</span>
  </article>

  <article class="card" style="left:297px">
    <h2>What's Speciality?</h2>
    <div role="img" aria-label="Photo of a man in a dark suit holding a handgun" style="height:264px;background:linear-gradient(#9aa2a8,#3c4146)"></div>
    <p class="caption">Mauris pretium metus eu arcu aliquet sit amet vulput ate eros suscipit.</p>
    <span class="more">Learn More</span>
  </article>

  <article class="card" style="left:497px">
    <h2>Recent Reviews</h2>
    <div class="card-photo" style="height:118px;background:linear-gradient(#d0d0d0,#5a4a44)" role="img" aria-label="Photo of a man in a black shirt aiming a pistol"></div>
    <div class="card-body">
      <p>Lorem ipsum dolor sit amet, conse ctetur adipis cing elit.Lorem ipsum dolor sit amet, conse ctetur adipis cing elit.Lorem ipsum dolor sit amet, conse ctetur adipis cing elit.</p>
      <p style="margin-top:8px;font-weight:700;color:#333">Mark Dalton, UAE</p>
    </div>
    <span class="more">Learn More</span>
  </article>

  <article class="card" style="left:696px">
    <h2>News Range</h2>
    <div class="news-item"><div class="news-date"><b>12</b>Jan</div><div><h3>Lorem ipsum dolor sit ame</h3><p>Vivamus felis augue, facilisis nec, tristique sed nulla.</p></div></div>
    <div class="news-item"><div class="news-date"><b>11</b>Jan</div><div><h3>Lorem ipsum dolor sit ame</h3><p>Vivamus felis augue, facilisis nec, tristique sed nulla.</p></div></div>
    <div class="news-item" style="border:0"><div class="news-date"><b>10</b>Jan</div><div><h3>Lorem ipsum dolor sit ame</h3><p>Lorem ipsum dolor sit amet, conse ctetur adipis cing elit.Lorem ipsum dolor sit amet, conse ctetur adipis cing</p></div></div>
    <span class="more">Learn More</span>
  </article>
</section>

<footer class="footer">
  <h4 class="foot-head" style="left:94px">True Mark Indoor Range Quick Links</h4>
  <ul class="links" style="left:109px">
    <li>Home</li><li>Why Us?</li><li>Contact Us</li><li>FAQ</li>
    <li class="gap">Live Chat</li><li>Testimonials</li><li>Our Corporate Reviews</li><li>New batch for the Month</li>
  </ul>
  <ul class="links" style="left:263px">
    <li>Range Fees</li><li>Range Rules</li><li>Range Support</li><li>Locate us</li>
    <li class="gap">Membership</li><li class="hot">Range Corporate Class</li><li>Collaboration &amp; Awards</li><li>News</li>
  </ul>
  <h4 class="foot-head" style="left:426px">Join Our Mail Listing</h4>
  <div class="mail">
    <p>Please enter you email address to subscribe</p>
    <div class="field"></div>
    <span class="subscribe">Subscribe</span>
    <div class="share"><span style="width:44px"></span><span style="width:30px;background:#fff"></span><span style="width:34px"></span><span style="width:30px"></span></div>
  </div>
  <div class="foot-brand"><span class="brand-name">TRUE MARK INDOOR RANGE</span><span class="brand-dot"></span></div>
  <div class="foot-rule"></div>
  <p class="copyright">Copyright - 2012. All right reserved.<br>All brand and product names are trademarks or registered trademarks of their respective companies.</p>
</footer>
</body>
</html>
```